Technology management company looking for a new website with a professional look

Brennick IT is a recently re-branded technology management company that is looking for a website design to match its personalized approach and friendly culture.

We would like to see a specialized, but related, page style for each of our main service offerings of:

• Commercial IT Support (This is our primary focus)
• Commercial Phone Systems (We partner with http://www.voxtrell.com/ for our phone systems)
• Point of Sale Systems (We partner with http://www.tillmora.com/ for our POS systems.
• Web Design
• Hollow Pine Computers (Our residential computer service offering, branded as Hollow Pine Computers)

The Hollow Pine Computers page should be build upon the Hollow Pine Computers logo, the other four pages should be branded as Brennick IT.

These five separate pages should have subtle, yet clearly defined links to one another. They should also each have a Home, Products, Service, and Company in the menu.

The website should have a clean design with professional appeal, but not appear too sterile or uninviting. It needs to have a simple, easy to navigate menu interface along the top. We would also like the site to be mobile friendly.

It should also allow us to easily tie in links to our social media pages (Facebook, LinkedIn, Twitter and Google+) and provide easy access to our contact information from each page.

This is a link to our old website www.hollowpinecomputers.com

We don't currently have copy available. The text and menu design should be easily editable and expandable so we can use the design to fit our copy.

In general we are looking for a concept we can modify to fit our needs.

We need this design to be available with layers in a .psd format.

Target Market(s)

Small to mid-size businesses.

Industry/Entity Type

Information Technology

Number of Pages Required

5+ page

Font styles to use
Sans Serif

Requirements
Must have
• Mobile Friendly
• Professional Type Face
• Unity between all pages
• .PSD Format
Nice to have
• Themed with our logo
Should not have
• Bubbly unprofessional typeface. No comic sans.

```html
<!DOCTYPE html>
<html lang="en">
<head>
<meta charset="utf-8">
<title>Brennick IT — Technology Management</title>
<link rel="stylesheet" href="https://fonts.googleapis.com/css2?family=Raleway:wght@300;400;600;700&family=Open+Sans:wght@400;600&display=swap">
<style>
:root{
  --orange:#f26522;
  --ink:#2e2e2e;
  --text:#6b6b6b;
  --muted:#9a9a9a;
  --line:#dcdcdc;
  --topbar:#2a2a2a;
  --footer:#1c1c1c;
  --hero-a:#f7f7f7;
  --hero-b:#e6e6e6;
  --panel:#f0f0f0;
  --white:#ffffff;
}
*{box-sizing:border-box;margin:0;padding:0}
html,body{width:800px;height:1200px;overflow:hidden}
body{font-family:"Open Sans",Arial,sans-serif;color:var(--text);background:var(--white);position:relative}
.heading{font-family:"Raleway",Arial,sans-serif}

/* top bar */
.topbar{height:18px;background:var(--topbar);display:flex;align-items:center;justify-content:space-between;padding:0 26px 0 40px}
.topbar-nav{display:flex;gap:34px;font-size:7px;letter-spacing:.8px;color:#bdbdbd;font-weight:600}
.topbar-nav a{color:inherit;text-decoration:none;padding:3px 8px}
.topbar-nav .is-active{background:var(--orange);color:var(--white)}
.topbar-social{display:flex;gap:14px}
.topbar-social span{width:9px;height:9px;border-radius:50%;background:#8c8c8c;display:block}

/* header */
.site-header{height:87px;display:flex;align-items:center;padding:0 32px 0 38px;border-bottom:1px solid var(--line)}
.brand{display:flex;align-items:center;gap:8px;font-family:"Raleway",Arial,sans-serif;font-weight:700;font-size:25px;color:var(--ink);width:250px}
.brand-dot{width:22px;height:22px;border-radius:50%;background:var(--orange)}
.main-nav{display:flex;flex:1}
.main-nav a{font-size:10px;line-height:1.3;color:var(--ink);text-decoration:none;padding:2px 16px;border-left:1px solid var(--line);width:115px}
.main-nav a:first-child{border-left:none}
.search{margin-left:auto}

/* hero */
.hero{height:270px;position:relative;background:linear-gradient(180deg,var(--hero-a),var(--hero-b));overflow:hidden}
.hero-copy{position:absolute;left:72px;top:76px;width:330px}
.hero-kicker{font-family:"Raleway",sans-serif;color:var(--orange);font-size:14px;font-weight:400;letter-spacing:.5px}
.hero-title{font-family:"Raleway",sans-serif;color:var(--orange);font-size:29px;font-weight:400;letter-spacing:.5px;margin-top:1px}
.hero-text{font-size:7.5px;line-height:1.5;color:var(--orange);margin-top:12px;width:210px}
.hero-button{display:inline-block;margin-top:14px;font-size:7px;letter-spacing:1px;color:var(--orange);border:1px solid var(--orange);border-radius:12px;padding:6px 22px}
.hero-photo{position:absolute;left:470px;top:0;width:310px;height:270px;background:radial-gradient(ellipse at 55% 55%,#cfcfcf 0%,#e4e4e4 55%,rgba(230,230,230,0) 75%)}
.hero-arrow{position:absolute;top:128px}
.hero-arrow.prev{left:44px}
.hero-arrow.next{right:28px}
.hero-dots{position:absolute;left:108px;top:218px;display:flex;gap:5px}
.hero-dots span{width:8px;height:8px;border-radius:50%;background:#cfcfcf}
.hero-dots .is-active{background:var(--orange)}

/* welcome */
.welcome{text-align:center;padding-top:50px}
.section-title{font-family:"Raleway",sans-serif;font-size:22px;font-weight:600;color:var(--ink);letter-spacing:1px}
.lead{font-size:7.5px;margin-top:5px;color:var(--text)}
.welcome-body{font-size:7px;line-height:1.6;width:560px;margin:12px auto 0;color:var(--muted)}

/* services */
.services{margin-top:30px;height:185px;background:var(--panel);display:flex;justify-content:center;border-top:1px solid var(--line);border-bottom:1px solid var(--line)}
.service{width:128px;display:flex;flex-direction:column;align-items:center;padding-top:30px;text-align:center}
.service.is-active{background:var(--white);border-top:3px solid #9fc3dc;box-shadow:0 2px 6px rgba(0,0,0,.12)}
.service-icon{height:56px;display:flex;align-items:center;justify-content:center}
.service-label{font-family:"Raleway",sans-serif;font-size:10px;line-height:1.3;color:var(--orange);letter-spacing:.5px;margin-top:16px;text-transform:uppercase}
.service.is-active .service-label{color:var(--ink);font-weight:700}

/* contact */
.contact{text-align:center;padding-top:28px}
.contact-intro{font-size:7.5px;margin-top:6px;color:var(--muted)}
.contact-card{margin:12px auto 0;width:693px;height:96px;border:1px solid var(--line);display:flex;align-items:center;padding:0 30px;text-align:left;gap:40px}
.contact-brand .brand{font-size:15px;width:auto;gap:6px}
.contact-brand .brand-dot{width:13px;height:13px}
.contact-col{font-size:7.5px;line-height:1.55;color:var(--text)}
.contact-col h4{font-size:7.5px;color:var(--orange);font-weight:600;letter-spacing:.5px}
.contact-row{display:flex;align-items:center;gap:6px}

/* footer */
.site-footer{position:absolute;left:0;top:935px;width:800px;height:265px;background:var(--footer);text-align:center;color:#8d8d8d}
.footer-nav{display:flex;justify-content:center;gap:70px;padding-top:24px;font-size:7.5px;letter-spacing:.8px;font-weight:600}
.footer-nav a{color:#cfcfcf;text-decoration:none}
.footer-nav .is-active{color:var(--orange)}
.footer-brand{display:flex;justify-content:center;margin-top:28px}
.footer-brand .brand{color:var(--white);font-size:20px;width:auto}
.footer-brand .brand-dot{width:17px;height:17px}
.copyright{font-size:7.5px;margin-top:10px}
.footer-text{font-size:6.5px;line-height:1.6;width:520px;margin:10px auto 0}
.footer-social{display:flex;justify-content:center;gap:26px;margin-top:22px}
.footer-social span{width:10px;height:10px;border-radius:50%;background:#a5a5a5;display:block}
.footer-links{font-size:7px;margin-top:26px;display:flex;justify-content:center;gap:10px}
.footer-links a{color:#cfcfcf}
</style>
</head>
<body>

<div class="topbar">
  <nav class="topbar-nav">
    <a class="is-active" href="#">HOME</a><a href="#">PRODUCTS</a><a href="#">SERVICE</a><a href="#">COMPANY</a>
  </nav>
  <div class="topbar-social"><span></span><span></span><span></span><span></span></div>
</div>

<header class="site-header">
  <div class="brand"><span class="brand-dot"></span>Brennick IT</div>
  <nav class="main-nav">
    <a href="#">Commercial<br>IT Support</a>
    <a href="#">Commercial<br>Phone Systems</a>
    <a href="#">Point of<br>Sale Systems</a>
    <a href="#">Hollow Pine<br>Computers</a>
  </nav>
  <svg class="search" width="20" height="20" viewBox="0 0 20 20"><circle cx="8" cy="8" r="6" fill="none" stroke="#555" stroke-width="2"/><line x1="12.5" y1="12.5" x2="18" y2="18" stroke="#555" stroke-width="2.4" stroke-linecap="round"/></svg>
</header>

<section class="hero">
  <div class="hero-photo" role="img" aria-label="Photo of a smiling businesswoman working at a laptop"></div>
  <div class="hero-copy">
    <p class="hero-kicker">SIT AMET</p>
    <h1 class="hero-title">LOREM IPSUM DOLOR</h1>
    <p class="hero-text">Ut enim ad minim veniam, quis nostrud exercitation ullamco laboris nisi ut aliquip ex ea commodo consequat.</p>
    <span class="hero-button">PRODUCTS</span>
  </div>
  <svg class="hero-arrow prev" width="10" height="16" viewBox="0 0 10 16"><polyline points="8,2 2,8 8,14" fill="none" stroke="#b5b5b5" stroke-width="2"/></svg>
  <svg class="hero-arrow next" width="10" height="16" viewBox="0 0 10 16"><polyline points="2,2 8,8 2,14" fill="none" stroke="#b5b5b5" stroke-width="2"/></svg>
  <div class="hero-dots"><span class="is-active"></span><span></span><span></span></div>
</section>

<section class="welcome">
  <h2 class="section-title">WELCOME</h2>
  <p class="lead">Our goal is to build a relationship with our clients, communicate clearly, and find timely, cost effective solutions to your needs.</p>
  <p class="welcome-body">Lorem ipsum dolor sit amet, consectetur adipiscing elit, sed do eiusmod tempor incididunt ut labore et dolore magna aliqua. Ut enim ad minim veniam, quis nostrud exercitation ullamco laboris nisi ut aliquip ex ea commodo consequat. Duis aute irure dolor in reprehenderit in voluptate velit esse cillum dolore eu fugiat nulla pariatur. Excepteur sint occaecat cupidatat non proident, sunt in culpa qui officia deserunt mollit anim id est laborum. Sed ut perspiciatis unde omnis iste natus error sit voluptatem accusantium doloremque laudantium, totam rem aperiam eaque ipsa quae ab illo inventore veritatis.</p>

  <div class="services">
    <div class="service">
      <div class="service-icon">
        <svg width="48" height="44" viewBox="0 0 48 44"><circle cx="18" cy="26" r="11" fill="none" stroke="#8a8a8a" stroke-width="5" stroke-dasharray="4 3"/><circle cx="18" cy="26" r="5" fill="#8a8a8a"/><circle cx="36" cy="12" r="7" fill="none" stroke="#8a8a8a" stroke-width="4" stroke-dasharray="3 2"/><circle cx="36" cy="12" r="3" fill="#8a8a8a"/></svg>
      </div>
      <p class="service-label">Commercial<br>IT Support</p>
    </div>
    <div class="service is-active">
      <div class="service-icon">
        <svg width="56" height="32" viewBox="0 0 56 32"><rect x="2" y="4" width="52" height="24" rx="3" fill="#cfd8df"/></svg>
      </div>
      <p class="service-label">Commercial<br>Phone Systems</p>
    </div>
    <div class="service">
      <div class="service-icon">
        <svg width="42" height="42" viewBox="0 0 42 42"><rect x="1" y="1" width="40" height="40" rx="4" fill="none" stroke="#8a8a8a" stroke-width="2"/><rect x="7" y="7" width="12" height="12" fill="#8a8a8a"/><rect x="23" y="7" width="12" height="12" fill="#8a8a8a"/><rect x="7" y="23" width="12" height="12" fill="#8a8a8a"/><rect x="23" y="23" width="12" height="12" fill="#8a8a8a"/></svg>
      </div>
      <p class="service-label">Point of<br>Sale Systems</p>
    </div>
    <div class="service">
      <div class="service-icon">
        <svg width="44" height="44" viewBox="0 0 44 44"><circle cx="22" cy="22" r="18" fill="#9a9a9a"/></svg>
      </div>
      <p class="service-label">Hollow Pine<br>Computers</p>
    </div>
  </div>
</section>

<section class="contact">
  <h2 class="section-title">CONTACT US</h2>
  <p class="contact-intro">Our goal is to build a relationship with our clients, communicate clearly, and find timely, cost effective solutions to your needs.</p>
  <div class="contact-card">
    <div class="contact-col contact-brand">
      <div class="brand"><span class="brand-dot"></span>Brennick IT</div>
      <h4 style="margin-top:8px">OFFICE ADDRESS</h4>
      <p>218 Harlow Road<br>Suite 4, Dunmore, OH 45011</p>
    </div>
    <div class="contact-col" style="margin-left:70px">
      <div class="contact-row"><svg width="8" height="8" viewBox="0 0 8 8"><path d="M1 1h2l1 2-1 1a4 4 0 0 0 1 1l1-1 2 1v2a6 6 0 0 1-6-6z" fill="#f26522"/></svg>(555) 014-2290</div>
      <div class="contact-row"><svg width="8" height="8" viewBox="0 0 8 8"><rect x=".5" y="1.5" width="7" height="5" fill="none" stroke="#f26522"/><polyline points=".5,1.5 4,4.5 7.5,1.5" fill="none" stroke="#f26522"/></svg>hello@brennickit.com</div>
      <div class="contact-row"><svg width="8" height="8" viewBox="0 0 8 8"><circle cx="4" cy="4" r="3.5" fill="none" stroke="#f26522"/></svg>www.brennickit.com</div>
    </div>
    <div class="contact-col" style="margin-left:90px">
      <h4>OFFICE HOURS</h4>
      <p>Monday-Friday 8am-5pm<br>Saturday: Call to Book</p>
    </div>
  </div>
</section>

<footer class="site-footer">
  <nav class="footer-nav">
    <a class="is-active" href="#">HOME</a><a href="#">PRODUCTS</a><a href="#">SERVICE</a><a href="#">COMPANY</a>
  </nav>
  <div class="footer-brand"><div class="brand"><span class="brand-dot"></span>Brennick IT</div></div>
  <p class="copyright">Copyright © 2015 Brennick IT. All Rights Reserved.</p>
  <p class="footer-text">Nemo enim ipsam voluptatem quia voluptas sit aspernatur aut odit aut fugit, sed quia consequuntur magni dolores eos qui ratione voluptatem sequi nesciunt. Neque porro quisquam est, qui dolorem ipsum quia dolor sit amet, consectetur, adipisci velit, sed quia non numquam eius modi tempora incidunt ut labore.</p>
  <div class="footer-social"><span></span><span></span><span></span></div>
  <p class="footer-links"><a href="#">Terms of use</a>|<a href="#">Privacy Policy</a>|<a href="#">Get Registered</a></p>
</footer>

</body>
</html>
```